Southport Billboard for Hiring more CDL drivers

I need a catch design for a bill board (size 10ft by 36 ft) to catch the attention for semi truck drivers.
In the design I want it to include:
-My company logo along with my website(brisklanefreighters.com) and my number(503-217-6095) for contact info.
-I also need it to say earn up to $90,000 a year
-I will send a few photos to choose from
-I need the logo to look clean and simple! I don't want it to be cluttered just clean, simple and catchy.!

Target Market(s)

CDL Class A holders
Semi Truck Drivers

Industry/Entity Type

Trucking Company

Font styles to use
Other font styles liked:
• a font to match my logo

Requirements
Must have
• "Make up to $90,000"
"brisklanefreighters.com"
"503-217-6095"

```html
<!DOCTYPE html>
<html lang="en">
<head>
<meta charset="utf-8">
<title>Brisklane Freighters – Driver Hiring Billboard</title>
<link href="https://fonts.googleapis.com/css2?family=League+Spartan:wght@600;700;800&display=swap" rel="stylesheet">
<style>
  :root {
    --navy: #1c2a3d;
    --ink: #1b2230;
    --grey: #6f6f6f;
    --white: #ffffff;
    --page: #ffffff;
    --sky-top: #9fb8cf;
    --trees: #7d7468;
    --asphalt: #3a3d42;
  }
  * { margin: 0; padding: 0; box-sizing: border-box; }
  html, body {
    width: 1200px; height: 1200px; overflow: hidden;
    background: var(--page);
    font-family: "League Spartan", "Futura", sans-serif;
  }
  .billboard {
    position: absolute; left: 40px; top: 445px;
    width: 1120px; height: 311px;
    background: var(--white);
    box-shadow: 0 3px 10px rgba(0,0,0,.25);
    overflow: hidden;
  }
  .billboard-art { position: absolute; inset: 0; width: 1120px; height: 311px; }
  .brand-name {
    position: absolute; left: 20px; top: 22px;
    font-size: 33px; font-weight: 800; letter-spacing: .5px;
    color: var(--ink); line-height: 1;
  }
  .headline { position: absolute; left: 19px; top: 88px; line-height: 1; }
  .headline-audience { font-size: 37px; font-weight: 700; color: var(--grey); }
  .headline-role { font-size: 38px; font-weight: 800; color: var(--ink); margin-top: 2px; }
  .headline-pay {
    margin-top: 12px; font-size: 33px; font-weight: 800; color: var(--ink);
    display: flex; gap: 30px;
  }
  .contact { position: absolute; left: 20px; top: 236px; color: var(--white); }
  .contact-row { display: flex; align-items: center; gap: 14px; line-height: 1; }
  .contact-phone { font-size: 37px; font-weight: 800; }
  .contact-web { font-size: 19px; font-weight: 700; margin-top: 9px; gap: 16px; padding-left: 3px; }
  .contact-icon { flex: none; }
</style>
</head>
<body>
  <section class="billboard">
    <svg class="billboard-art" viewBox="0 0 1120 311" xmlns="http://www.w3.org/2000/svg">
      <defs>
        <linearGradient id="photoTones" x1="0" y1="0" x2="0" y2="1">
          <stop offset="0" stop-color="var(--sky-top)"/>
          <stop offset=".35" stop-color="var(--trees)"/>
          <stop offset=".7" stop-color="#8e9c98"/>
          <stop offset="1" stop-color="var(--asphalt)"/>
        </linearGradient>
      </defs>
      <polygon class="contact-band" points="0,227 600,227 571,311 0,311" fill="var(--navy)"/>
      <polygon class="accent-stripe" points="678,0 694,0 636,102" fill="var(--navy)"/>
      <polygon class="truck-photo" role="img"
        aria-label="Photo of a pale green semi truck pulling a tarped flatbed load in a lot with bare trees behind"
        points="697,0 1120,0 1120,311 578,311" fill="url(#photoTones)"/>
    </svg>

    <div class="brand-name">BRISKLANE FREIGHTERS</div>

    <div class="headline">
      <div class="headline-audience">CDL CLASS A HOLDERS</div>
      <div class="headline-role">SEMI TRUCK DRIVERS</div>
      <div class="headline-pay"><span>MAKE UP TO</span><span>$90,000</span></div>
    </div>

    <div class="contact">
      <div class="contact-row contact-phone">
        <svg class="contact-icon" width="24" height="24" viewBox="0 0 24 24" aria-hidden="true">
          <path fill="#fff" d="M6.6 10.8a15.1 15.1 0 0 0 6.6 6.6l2.2-2.2c.3-.3.7-.4 1-.2 1.1.4 2.3.6 3.6.6.6 0 1 .4 1 1V20c0 .6-.4 1-1 1A17 17 0 0 1 3 4c0-.6.4-1 1-1h3.5c.6 0 1 .4 1 1 0 1.3.2 2.5.6 3.6.1.3 0 .7-.2 1z"/>
        </svg>
        <span>503-217-6095</span>
      </div>
      <div class="contact-row contact-web">
        <svg class="contact-icon" width="20" height="20" viewBox="0 0 20 20" aria-hidden="true">
          <g fill="none" stroke="#fff" stroke-width="1.6">
            <circle cx="10" cy="10" r="8.5"/>
            <ellipse cx="10" cy="10" rx="3.8" ry="8.5"/>
            <line x1="1.5" y1="10" x2="18.5" y2="10"/>
            <line x1="3" y1="5.5" x2="17" y2="5.5"/>
            <line x1="3" y1="14.5" x2="17" y2="14.5"/>
          </g>
        </svg>
        <span>www.brisklanefreighters.com</span>
      </div>
    </div>
  </section>
</body>
</html>
```